Property risk and finance brokerage company needs a business card design

Tarlow Financial requires a business card design. Please integrate existing logo (refer uploaded file).
hex codes used on logo #002649 #008ED6 #444F51 #ADAFAA
font used - Cinzel
Contact information
Renata Sollisford
Director
Mobile: 0491 738 205
email: r.sollisford@tarlowfinancial.example.au
website: www.tarlowfinancial.example.au
CRN : 918354
PO Box 527
Millbrook, Victoria, 3999
Horizontal orientation please
Finance

```html
<!DOCTYPE html>
<html lang="en">
<head>
<meta charset="utf-8">
<title>Tarlow Financial – Business Card</title>
<link rel="stylesheet" href="https://fonts.googleapis.com/css2?family=Cinzel:wght@400;600&display=swap">
<style>
  :root {
    --stage: #1b1b1d;
    --navy: #002649;
    --sky: #008ed6;
    --band: #1f5b92;
    --slate: #444f51;
    --stone: #adafaa;
    --panel: #7c7471;
    --paper: #ffffff;
    --mist: #eef1f7;
    --wood-light: #9a7c62;
    --wood-dark: #7a5d47;
    --ember: #d2552a;
    --ink: #2b2b2b;
  }
  * { box-sizing: border-box; margin: 0; padding: 0; }
  html, body { width: 1200px; height: 1112px; overflow: hidden; }
  body {
    background: var(--stage);
    font-family: "Cinzel", serif;
    position: relative;
  }
  .card {
    position: absolute;
    left: 190px;
    width: 820px;
    height: 500px;
    overflow: hidden;
  }

  /* Details side */
  .card-details { top: 37px; background: var(--paper); }
  .side-panel {
    position: absolute; left: 0; top: 0;
    width: 310px; height: 392px;
    background: var(--panel);
  }
  .brand-mark {
    position: absolute; right: 34px; top: 46px;
    display: flex; align-items: center; gap: 12px;
    color: var(--slate); font-weight: 400;
    font-size: 26px; line-height: 1.05; letter-spacing: 1px;
  }
  .brand-mark .dot {
    width: 34px; height: 34px; border-radius: 50%;
    background: var(--stone);
  }
  .name {
    position: absolute; top: 142px; left: 0; width: 100%;
    font-size: 38px; letter-spacing: 2px; text-transform: uppercase;
    white-space: nowrap;
  }
  .name .first { position: absolute; right: 522px; color: #f2efee; }
  .name .last { position: absolute; left: 322px; color: var(--band); }
  .role {
    position: absolute; left: 324px; top: 194px;
    font-size: 16px; letter-spacing: 1.5px; color: var(--slate);
  }
  .contacts {
    position: absolute; left: 340px; top: 258px;
    display: grid; grid-template-columns: 104px auto;
    row-gap: 14px; column-gap: 12px; align-items: center;
  }
  .contacts .label {
    background: var(--band); color: var(--paper);
    font-size: 10px; letter-spacing: 0.5px;
    padding: 5px 6px; text-align: center; white-space: nowrap;
  }
  .contacts .value { font-size: 12px; color: var(--ink); white-space: nowrap; }
  .info-band {
    position: absolute; left: 0; top: 392px;
    width: 100%; height: 62px; background: var(--band);
  }
  .info-band .web {
    position: absolute; left: 24px; top: 22px;
    color: var(--paper); font-size: 15px; letter-spacing: 1px;
  }
  .info-band .postal {
    position: absolute; left: 520px; top: 12px;
    color: var(--paper); font-size: 12px; line-height: 1.5; white-space: nowrap;
  }
  .info-band .seal {
    position: absolute; right: 26px; top: 7px;
    width: 48px; height: 48px; border-radius: 50%;
    background: var(--ember); border: 3px solid var(--paper);
  }
  .edge-strip {
    position: absolute; left: 0; top: 464px;
    width: 100%; height: 10px; background: var(--band);
  }

  /* Logo side */
  .card-front { top: 574px; background: var(--mist); }
  .front-mark {
    position: absolute; left: 0; top: 0; width: 100%; height: 395px;
    display: flex; align-items: center; justify-content: center; gap: 20px;
  }
  .front-mark .dot {
    width: 64px; height: 64px; border-radius: 50%; background: var(--navy);
  }
  .front-mark .wordmark {
    color: var(--ink); font-weight: 400;
    font-size: 50px; line-height: 1.05; letter-spacing: 2px;
  }
  .wood-strip {
    position: absolute; left: 0; bottom: 0; width: 100%; height: 105px;
    background: linear-gradient(90deg, var(--wood-light), var(--wood-dark) 50%, var(--wood-light));
  }
</style>
</head>
<body>

<section class="card card-details">
  <div class="side-panel"></div>
  <div class="brand-mark">
    <span class="dot"></span>
    <span>TARLOW<br>FINANCIAL</span>
  </div>
  <div class="name">
    <span class="first">Renata</span>
    <span class="last">Sollisford</span>
  </div>
  <div class="role">MANAGING DIRECTOR</div>
  <div class="contacts">
    <span class="label">MOBILE</span><span class="value">0491 738 205</span>
    <span class="label">EMAIL</span><span class="value">r.sollisford@tarlowfinancial.example.au</span>
    <span class="label">CREDIT REP NO.</span><span class="value">918354</span>
  </div>
  <div class="info-band">
    <span class="web">www.tarlowfinancial.example.au</span>
    <span class="postal">PO Box 527<br>Millbrook, Victoria, 3999</span>
    <span class="seal"></span>
  </div>
  <div class="edge-strip"></div>
</section>

<section class="card card-front">
  <div class="front-mark">
    <span class="dot"></span>
    <span class="wordmark">TARLOW<br>FINANCIAL</span>
  </div>
  <div class="wood-strip" role="img" aria-label="Warm timber floorboard texture strip"></div>
</section>

</body>
</html>
```